Kelvo Mist business cards + chance to win packaging and other design projects

including logo already designed.

******** I need 2 business cards:
1. that is general for the company
2. that is specific for me

*********On the reverse side of the business card I want it to be divided into 4 boxes and each box to describe a stage in how to use the product. I need the boxes to be numbered and the contents to be easy to absorb and include graphics showing the actions also.
Turning then photo's into simplified, cool illustrations** would be really cool. This would allow changes, like writing "water" on the bottle etc etc. Maybe have a fftness lady drinking at the end? Imagination over to you.
The photo's are of the prototype so the illustrations can replace the grey caps with bright orange etc etc

CAPTIONS FOR ILLUSTRATIONS
1. Charge the Kelvo Mist
2.The Kelvo Mist is now ready for making a shake anywhere, anytime !
3. Choose any bottled water or beverage, release shot cap and Jet powder in.
4. Shake bottle, enjoy!
Updates

Can you illustrate?
I just changed the photos and captions to simplify.
Please re read the brief, thanks

Target Market(s)

Fitness, weight loss, health
male and female
any potential powdered drink user.

orvan, tindair design style ? Clean, simple, bold, clever, cool

Industry/Entity Type

Business

Requirements
Must have
• Must have logo and kelvomist.com

Card 1: email: info@kelvomist.com

Card 2: Reuben Hallowby LL.b. /President/ email:reuben@kelvomist.com/ office: 555 018 4431/ direct: 555 014 7820

I want the card to have a white background, not color blocked in.

I have included photos of the type of illustrations needed in each box.
In the illustrations pls make the kelvo mist army green and the caps bright orange.
Get the point across as simply as you can. Make it cool pls :)

```html
<!DOCTYPE html>
<html lang="en">
<head>
<meta charset="utf-8">
<title>Kelvo Mist business cards</title>
<link rel="stylesheet" href="https://fonts.googleapis.com/css2?family=Questrial&display=swap">
<style>
  :root {
    --stage: #eeeeee;
    --card: #ffffff;
    --orange: #f26522;
    --navy: #2b3a67;
    --navy-tint: #c9cdd9;
    --text: #4a4a4a;
    --muted: #5c5c5c;
    --panel: #e4e4e4;
    --bubble: #e2e2e2;
    --shadow: rgba(0, 0, 0, 0.22);
  }
  * { box-sizing: border-box; margin: 0; padding: 0; }
  html, body {
    width: 1200px;
    height: 728px;
    overflow: hidden;
    background: var(--stage);
    font-family: "Questrial", "Century Gothic", sans-serif;
  }
  .canvas {
    position: relative;
    width: 1200px;
    height: 728px;
  }
  .card {
    position: absolute;
    width: 476px;
    height: 292px;
    background: var(--card);
    box-shadow: 0 2px 5px var(--shadow);
    overflow: hidden;
  }
  .card--front { left: 95px; top: 89px; }
  .card--back { left: 629px; top: 304px; }

  .bubble-field {
    position: absolute;
    border-radius: 50%;
    background: radial-gradient(ellipse at center, var(--bubble) 0%, rgba(226,226,226,0.55) 45%, rgba(255,255,255,0) 72%);
  }
  .card--front .bubble-field { left: 150px; top: 20px; width: 330px; height: 250px; }
  .card--back .bubble-field { left: 330px; top: 40px; width: 170px; height: 170px; }

  .wordmark {
    position: absolute;
    left: 0;
    width: 100%;
    top: 104px;
    display: flex;
    justify-content: center;
    align-items: center;
    gap: 10px;
    color: var(--orange);
    font-size: 40px;
    letter-spacing: 1px;
    text-transform: uppercase;
  }
  .wordmark__dot {
    width: 12px;
    height: 12px;
    border-radius: 50%;
    background: var(--orange);
  }
  .web-address {
    position: absolute;
    left: 0;
    width: 100%;
    top: 250px;
    text-align: center;
    color: var(--muted);
    font-size: 15px;
    letter-spacing: 0.3px;
  }

  .steps {
    position: absolute;
    left: 24px;
    top: 27px;
    width: 237px;
    height: 241px;
    background: var(--panel);
  }
  .step-art {
    position: absolute;
    border-radius: 6px;
    background: radial-gradient(ellipse at center, var(--navy-tint) 0%, rgba(201,205,217,0.35) 70%, rgba(228,228,228,0) 100%);
  }
  .step-art--1 { left: 16px; top: 20px; width: 76px; height: 82px; }
  .step-art--2 { left: 138px; top: 30px; width: 72px; height: 62px; }
  .step-art--3 { left: 12px; top: 122px; width: 76px; height: 88px; }
  .step-art--4 { left: 124px; top: 146px; width: 98px; height: 62px; }

  .step-number {
    position: absolute;
    width: 12px;
    height: 12px;
    border-radius: 50%;
    background: var(--orange);
    color: #fff;
    font-size: 8px;
    line-height: 12px;
    text-align: center;
  }
  .step-number--1 { left: 49px; top: 108px; }
  .step-number--2 { left: 166px; top: 108px; }
  .step-number--3 { left: 44px; top: 214px; }
  .step-number--4 { left: 166px; top: 214px; }

  .holder {
    position: absolute;
    left: 278px;
    top: 32px;
    white-space: nowrap;
  }
  .holder__name {
    color: var(--orange);
    font-size: 17px;
    font-weight: 400;
    letter-spacing: 0.2px;
  }
  .holder__title {
    margin-top: 12px;
    color: var(--text);
    font-size: 14px;
  }

  .contacts {
    position: absolute;
    left: 278px;
    top: 182px;
    list-style: none;
  }
  .contacts__item {
    display: flex;
    align-items: center;
    gap: 9px;
    height: 30px;
    color: var(--text);
    font-size: 15px;
    white-space: nowrap;
  }
  .contacts__icon {
    width: 16px;
    height: 16px;
    fill: var(--navy);
    flex: none;
  }
</style>
</head>
<body>
<main class="canvas">

  <section class="card card--front" aria-label="Company card">
    <div class="bubble-field" role="img" aria-label="Soft grey bubble decoration"></div>
    <div class="wordmark"><span class="wordmark__dot"></span><span>Kelvo Mist</span></div>
    <p class="web-address">www. kelvomist.com</p>
  </section>

  <section class="card card--back" aria-label="Personal card">
    <div class="bubble-field" role="img" aria-label="Soft grey bubble decoration"></div>
    <div class="steps" aria-label="How to use, in four steps">
      <div class="step-art step-art--1" role="img" aria-label="Step 1 illustration: a hand scooping powder into the shot cap"></div>
      <div class="step-art step-art--2" role="img" aria-label="Step 2 illustration: a hand holding the charged cap, ready to go"></div>
      <div class="step-art step-art--3" role="img" aria-label="Step 3 illustration: hands fitting the cap to a water bottle and releasing the powder"></div>
      <div class="step-art step-art--4" role="img" aria-label="Step 4 illustration: drinking the shaken bottle"></div>
      <span class="step-number step-number--1">1</span>
      <span class="step-number step-number--2">2</span>
      <span class="step-number step-number--3">3</span>
      <span class="step-number step-number--4">4</span>
    </div>

    <div class="holder">
      <h1 class="holder__name">Reuben Hallowby LL.b.</h1>
      <p class="holder__title">President</p>
    </div>

    <ul class="contacts">
      <li class="contacts__item">
        <svg class="contacts__icon" viewBox="0 0 16 16" aria-hidden="true">
          <path d="M1 6c0-2 3-3.5 7-3.5S15 4 15 6v1.2h-3.4V5.8c-1-.4-2.4-.6-3.6-.6s-2.6.2-3.6.6v1.4H1z"/>
          <path d="M3.5 8.2 5 7h6l1.5 1.2V14h-9z"/>
        </svg>
        <span>555 018 4431</span>
      </li>
      <li class="contacts__item">
        <svg class="contacts__icon" viewBox="0 0 16 16" aria-hidden="true">
          <path d="M3.6 1.5 5.8 4 4.6 5.6c.8 2 2.4 3.6 4.4 4.4L10.6 8.8 13 11l-1.4 2.6C6.6 13.4 2.6 9.4 2.4 4.4z"/>
          <path d="M9 1.5a5.5 5.5 0 0 1 5.5 5.5h-1.2A4.3 4.3 0 0 0 9 2.7zM9 4a3 3 0 0 1 3 3h-1.2A1.8 1.8 0 0 0 9 5.2z"/>
        </svg>
        <span>555 014 7820</span>
      </li>
      <li class="contacts__item">
        <svg class="contacts__icon" viewBox="0 0 16 16" aria-hidden="true">
          <path d="M1 3.5h14v9H1zm1.4 1.2v.2L8 9l5.6-4.1v-.2zM2.2 6.3v5h11.6v-5L8 10.5z"/>
        </svg>
        <span>reuben@kelvomist.com</span>
      </li>
    </ul>
  </section>

</main>
</body>
</html>
```